Wild Ridge Trekcraft DL flyer

I'm looking for a new flyer for my startup business. In Darwin Australia.
Aimed at family's and short stay tourists the "Wild Ridge Trekcraft" 4 hr tour will give people a basic understanding of some essential bush survival skills in the Australian Outback.
things covered in this 4 hr tour are
1. Finding water.
2. finding food.
3. Finding/making shelter and fire.
4. Finding your way home.

The tour will pick clients up in an air conditioned purpose build 4WD and take them to a nearby bushland area where they will have the opportunity to catch and harvest some native bushtucker.
They will then be able to find/harvest some water for survival situations.
While we cook our bush tucker they will also learn to find their way home through ancient navigation techniques as well.

Clients will then be dropped back to their accomodation with some fun and vital knowledge of surviving in the Australian outback.
At the end of the tour the group will be able to take home a basic survival kit which they will be able to use through the skills they just gained on the tour.

I'd like a two sided DL size flyer emphasising the following points.
4hr/half day tour
Fun for the family
Free survival kit included.
Eat what you catch
Learn essential survival skills
Provided buy an experienced and passionate bushman.
$150/head including transfers.

I'll provide some pictures for the flyer and any extra content you require.
Updates

Target Market(s)

Family's
Short stay tourists

Industry/Entity Type

Tourism

Colors

Designer to choose colors to be used in the design.

Requirements
Must have
• As per brief
Nice to have
• Any extra content and flair designers would like to add
Should not have
• Any images which aren't Australian

```html
<!DOCTYPE html>
<html lang="en">
<head>
<meta charset="utf-8">
<title>Wild Ridge Trekcraft – DL Flyer</title>
<link href="https://fonts.googleapis.com/css2?family=Roboto+Condensed:wght@700&family=Open+Sans:wght@400;600&display=swap" rel="stylesheet">
<style>
  :root {
    --page-bg: #e9e6e1;
    --green: #16a57a;
    --green-deep: #087049;
    --cell-a: #159a71;
    --cell-b: #22ab82;
    --cream: #f3f5ea;
    --ink: #2f3a33;
    --tick: #1b9e6e;
    --white: #ffffff;
    --photo-crayfish: linear-gradient(150deg, #8a7f73, #b99b86 45%, #4a4640);
    --photo-net: linear-gradient(160deg, #214a1c, #3f7a2c 55%, #5ea23a);
    --photo-fruit: linear-gradient(140deg, #b8a090, #8e9a55 50%, #c9b3a3);
    --photo-palm: linear-gradient(150deg, #1f4a1a, #3d7a2a 50%, #2a5a20);
    --photo-mounds: linear-gradient(180deg, #9fc0e2 0%, #6b8f55 35%, #8a5a32 65%, #6f9a3c 100%);
  }
  * { box-sizing: border-box; margin: 0; padding: 0; }
  html, body { width: 1020px; height: 1200px; overflow: hidden; }
  body { background: var(--page-bg); position: relative; font-family: "Open Sans", sans-serif; }

  .flyer {
    position: absolute; left: 230px; top: 40px;
    width: 560px; height: 1120px;
    background: var(--white);
    box-shadow: 0 4px 14px rgba(0,0,0,.25);
    overflow: hidden;
  }
  .flyer-header {
    position: absolute; left: 0; top: 0; width: 560px; height: 116px;
    background: var(--green);
    display: flex; align-items: center; justify-content: center;
  }
  .flyer-title {
    font-family: "Roboto Condensed", sans-serif; font-weight: 700;
    font-size: 46px; color: var(--white); letter-spacing: .5px;
    text-shadow: 2px 2px 2px rgba(0,0,0,.45);
  }

  .photo { position: absolute; }
  .photo-crayfish { left: 0; top: 122px; width: 277px; height: 226px; background: var(--photo-crayfish); }
  .photo-net { left: 283px; top: 122px; width: 277px; height: 186px; background: var(--photo-net); }
  .photo-fruit { left: 0; top: 354px; width: 135px; height: 150px; background: var(--photo-fruit); }
  .photo-palm { left: 141px; top: 354px; width: 136px; height: 150px; background: var(--photo-palm); }
  .photo-mounds { left: 283px; top: 314px; width: 277px; height: 190px; background: var(--photo-mounds); }

  .skills {
    position: absolute; left: 0; top: 510px; width: 560px; height: 128px;
    display: flex;
  }
  .skill {
    flex: 1; display: flex; flex-direction: column; align-items: center;
    color: var(--white); text-align: center; padding-top: 22px;
    font-size: 16px; line-height: 1.3;
  }
  .skill:nth-child(odd) { background: var(--cell-a); }
  .skill:nth-child(even) { background: var(--cell-b); }
  .skill-icon { width: 52px; height: 46px; margin-bottom: 12px; }
  .skill-label { min-height: 42px; display: flex; align-items: center; }

  .services {
    position: absolute; left: 0; top: 638px; width: 560px; height: 420px;
    background: var(--cream);
  }
  .services-badge {
    position: absolute; left: 182px; top: 19px; width: 193px; height: 43px;
    border-radius: 8px;
    background: linear-gradient(180deg, #27b486, #12935f);
    box-shadow: 0 2px 3px rgba(0,0,0,.25);
    color: var(--white); font-size: 21px;
    display: flex; align-items: center; justify-content: center;
  }
  .service-list {
    position: absolute; left: 28px; top: 90px; width: 300px;
    list-style: none; font-size: 16px; color: var(--ink);
  }
  .service-list li {
    position: relative; padding-left: 28px; line-height: 22px; margin-bottom: 5.5px;
  }
  .service-list svg { position: absolute; left: 0; top: 4px; width: 15px; height: 14px; }

  .bubble {
    position: absolute; border-radius: 50%;
    border: 5px solid var(--green);
    box-shadow: 0 2px 4px rgba(0,0,0,.2);
  }
  .bubble-fruit { left: 273px; top: 78px; width: 140px; height: 140px;
    background: linear-gradient(150deg, #7fa6c8, #6a5a3a 55%, #d39a2a); }
  .bubble-guide { left: 405px; top: 80px; width: 128px; height: 128px;
    background: linear-gradient(160deg, #dfe8ee, #9a8a72 55%, #5d6a50); }
  .bubble-catch { left: 351px; top: 167px; width: 140px; height: 140px;
    background: linear-gradient(150deg, #5e8a4a, #a2775a 50%, #3f5e3a); }

  .flyer-footer { position: absolute; left: 0; top: 960px; width: 560px; height: 160px; }
  .footer-waves { position: absolute; inset: 0; width: 560px; height: 160px; }
  .footer-contact {
    position: absolute; left: 0; top: 68px; width: 560px; text-align: center; color: var(--white);
  }
  .footer-phone { font-family: "Roboto Condensed", sans-serif; font-weight: 700; font-size: 31px; }
  .footer-phone .call { font-size: 23px; }
  .footer-web { margin-top: 2px; font-size: 18px; display: flex; align-items: center; justify-content: center; gap: 6px; }
  .footer-web .dot { width: 13px; height: 13px; border: 2px solid var(--white); border-radius: 50%; }
  .footer-rule { width: 360px; height: 1px; margin: 8px auto 0; background: rgba(255,255,255,.45); }
</style>
</head>
<body>
  <main class="flyer">
    <header class="flyer-header">
      <h1 class="flyer-title">Wild Ridge Trekcraft</h1>
    </header>

    <div class="photo photo-crayfish" role="img" aria-label="Photo: freshwater crayfish held in open hands"></div>
    <div class="photo photo-net" role="img" aria-label="Photo: plastic bag tied over leafy branch to collect water"></div>
    <div class="photo photo-fruit" role="img" aria-label="Photo: small green bush fruits in a palm"></div>
    <div class="photo photo-palm" role="img" aria-label="Photo: pandanus palm leaves"></div>
    <div class="photo photo-mounds" role="img" aria-label="Photo: termite mounds in outback grassland"></div>

    <section class="skills">
      <div class="skill">
        <svg class="skill-icon" viewBox="0 0 52 46"><path d="M26 4 C20 14 15 20 15 28 a11 11 0 0 0 22 0 C37 20 32 14 26 4Z" fill="#fff"/></svg>
        <span class="skill-label">Finding water</span>
      </div>
      <div class="skill">
        <svg class="skill-icon" viewBox="0 0 52 46"><circle cx="30" cy="9" r="3" fill="#fff"/><path d="M14 28 a16 16 0 0 1 32 0Z" fill="#fff"/><rect x="11" y="30" width="38" height="3" fill="#fff"/><path d="M4 40 h8 l6-4 h14 v3 h-12 l-6 5 h-10Z" fill="#fff"/></svg>
        <span class="skill-label">Finding Food</span>
      </div>
      <div class="skill">
        <svg class="skill-icon" viewBox="0 0 52 46"><path d="M26 4 l11 9 v12 h-22 v-12Z" fill="#fff"/><rect x="22" y="15" width="8" height="6" fill="var(--cell-a)"/><path d="M4 18 l4 14 l10 10 h6 v-6 l-8-8 l-4-10Z M48 18 l-4 14 l-10 10 h-6 v-6 l8-8 l4-10Z" fill="none" stroke="#fff" stroke-width="2.5" stroke-linejoin="round"/></svg>
        <span class="skill-label">Finding/Making<br>Shelter and Fire</span>
      </div>
      <div class="skill">
        <svg class="skill-icon" viewBox="0 0 52 46"><path d="M26 4 L48 23 h-6 v19 h-10 v-12 h-12 v12 h-10 v-19 h-6Z" fill="#fff"/></svg>
        <span class="skill-label">Finding your<br>way Home</span>
      </div>
    </section>

    <section class="services">
      <div class="services-badge">OUR SERVICES</div>
      <ul class="service-list">
        <li><svg viewBox="0 0 15 14"><path d="M1 8 l4 4 l9-11" fill="none" stroke="var(--tick)" stroke-width="2"/></svg>4hr/half day tour</li>
        <li><svg viewBox="0 0 15 14"><path d="M1 8 l4 4 l9-11" fill="none" stroke="var(--tick)" stroke-width="2"/></svg>Fun for the family</li>
        <li><svg viewBox="0 0 15 14"><path d="M1 8 l4 4 l9-11" fill="none" stroke="var(--tick)" stroke-width="2"/></svg>Free survival kit included</li>
        <li><svg viewBox="0 0 15 14"><path d="M1 8 l4 4 l9-11" fill="none" stroke="var(--tick)" stroke-width="2"/></svg>Eat what you catch</li>
        <li><svg viewBox="0 0 15 14"><path d="M1 8 l4 4 l9-11" fill="none" stroke="var(--tick)" stroke-width="2"/></svg>Learn essential survival skills</li>
        <li><svg viewBox="0 0 15 14"><path d="M1 8 l4 4 l9-11" fill="none" stroke="var(--tick)" stroke-width="2"/></svg>Provided buy an experienced<br>and passionate bushman</li>
        <li><svg viewBox="0 0 15 14"><path d="M1 8 l4 4 l9-11" fill="none" stroke="var(--tick)" stroke-width="2"/></svg>$150/head including transfers</li>
      </ul>
      <div class="bubble bubble-fruit" role="img" aria-label="Photo: bush fruit hanging from a branch"></div>
      <div class="bubble bubble-guide" role="img" aria-label="Photo: bushman guide in a wide-brim hat"></div>
      <div class="bubble bubble-catch" role="img" aria-label="Photo: guide holding up a freshly caught mud crab"></div>
    </section>

    <footer class="flyer-footer">
      <svg class="footer-waves" viewBox="0 0 560 160" preserveAspectRatio="none">
        <path d="M0 55 Q280 -5 560 12 L560 60 Q300 35 0 88Z" fill="var(--green-deep)"/>
        <path d="M0 92 Q290 40 560 62 L560 160 L0 160Z" fill="var(--green)"/>
        <path d="M0 88 Q300 35 560 60" fill="none" stroke="#fff" stroke-width="3"/>
      </svg>
      <div class="footer-contact">
        <div class="footer-phone"><span class="call">CALL NOW:</span>0400 555 018</div>
        <div class="footer-web"><span class="dot"></span>www.wildridge.com</div>
        <div class="footer-rule"></div>
      </div>
    </footer>
  </main>
</body>
</html>
```